Kelvano Business cards

Dunja hajde Molim te nam napravi neke Super biznis vizitke. Moze sa obe strane print.
Luka Brankov
CEO - Senior Consultant
Mail: lb@kelvano-mail.rs
Phone: +43 660 529 304 7

Zorana Medaka 14. Birkenhofweg 9b
26480 Velin Brod. 3356 Haselbrunn
Serbia. Austria

```html
<!DOCTYPE html>
<html lang="en">
<head>
<meta charset="utf-8">
<title>Kelvano Business Cards</title>
<link rel="stylesheet" href="https://fonts.googleapis.com/css2?family=Orbitron:wght@700&family=Exo+2:wght@400;500&display=swap">
<style>
  :root {
    --stage: #d8d2ca;
    --card-dark: #4a4a4a;
    --card-light: #e3e3e3;
    --accent: #f0b428;
    --ink-light: #ffffff;
    --ink-dark: #4a4a4a;
  }
  * { margin: 0; padding: 0; box-sizing: border-box; }
  html, body {
    width: 1200px;
    height: 674px;
    overflow: hidden;
    background: var(--stage);
  }
  .canvas {
    position: relative;
    width: 1200px;
    height: 674px;
  }
  .card {
    position: absolute;
    left: 399px;
    width: 390px;
    height: 223px;
    overflow: hidden;
  }
  .card--front { top: 105px; background: var(--card-dark); }
  .card--back { top: 360px; background: var(--card-light); }

  .logo-text {
    position: absolute;
    font-family: "Orbitron", sans-serif;
    font-weight: 700;
    text-transform: uppercase;
    line-height: 1.45;
    letter-spacing: 0.04em;
    transform: skewX(-14deg);
  }
  .card--front .logo-text {
    left: 0;
    width: 100%;
    top: 82px;
    font-size: 25px;
    color: var(--accent);
    text-align: center;
  }
  .card--front .logo-text span { display: block; }
  .card--front .logo-text .logo-line-2 { padding-left: 14px; }

  .card--back .logo-text {
    left: 28px;
    top: 32px;
    font-size: 14px;
    color: var(--ink-dark);
  }
  .card--back .logo-text span { display: block; }
  .card--back .logo-text .logo-line-2 { padding-left: 12px; }

  .swoosh { position: absolute; inset: 0; width: 390px; height: 223px; }
  .swoosh .panel { fill: var(--card-dark); }
  .swoosh .band { fill: var(--accent); }

  .identity {
    position: absolute;
    left: 258px;
    top: 55px;
    font-family: "Exo 2", sans-serif;
  }
  .identity .name {
    font-size: 13px;
    font-weight: 400;
    color: var(--ink-light);
    text-transform: uppercase;
    letter-spacing: 0.08em;
  }
  .identity .role {
    font-size: 7px;
    color: var(--accent);
    text-transform: lowercase;
    letter-spacing: 0.04em;
    margin-top: 1px;
  }

  .contact {
    position: absolute;
    right: 22px;
    font-family: "Exo 2", sans-serif;
    font-size: 6.5px;
    color: var(--ink-light);
    display: flex;
    align-items: center;
    gap: 6px;
  }
  .contact--mail { top: 143px; }
  .contact--phone { top: 159px; }
  .contact svg { width: 8px; height: 8px; fill: var(--accent); }

  .address {
    position: absolute;
    left: 224px;
    top: 187px;
    font-family: "Exo 2", sans-serif;
    font-style: normal;
    font-size: 6px;
    line-height: 1.75;
    color: var(--ink-light);
  }
</style>
</head>
<body>
<main class="canvas">

  <section class="card card--front" aria-label="Business card front">
    <p class="logo-text">
      <span class="logo-line-1">Your Logo</span>
      <span class="logo-line-2">Here</span>
    </p>
  </section>

  <section class="card card--back" aria-label="Business card back">
    <svg class="swoosh" viewBox="0 0 390 223" aria-hidden="true">
      <path class="panel" d="M334,0 C244,68 152,148 110,223 L390,223 L390,0 Z"/>
      <path class="band" d="M318,0 C232,62 134,150 92,223 L112,223 C154,148 246,68 336,0 Z"/>
    </svg>

    <p class="logo-text">
      <span class="logo-line-1">Your Logo</span>
      <span class="logo-line-2">Here</span>
    </p>

    <div class="identity">
      <p class="name">Luka Brankov</p>
      <p class="role">CEO - Senior Consultant</p>
    </div>

    <p class="contact contact--mail">
      <span>lb@kelvano-mail.rs</span>
      <svg viewBox="0 0 10 8" aria-hidden="true"><rect x="0" y="0" width="10" height="8" rx="1"/><path d="M0.8,1 L5,4.4 L9.2,1" fill="none" stroke="#4a4a4a" stroke-width="0.9"/></svg>
    </p>
    <p class="contact contact--phone">
      <span>+43 660 529 304 7</span>
      <svg viewBox="0 0 10 10" aria-hidden="true"><path d="M2.2,0.6 L3.9,2.6 L2.9,3.8 C3.6,5.3 4.7,6.4 6.2,7.1 L7.4,6.1 L9.4,7.8 L8.4,9.4 C4.4,9.2 0.8,5.6 0.6,1.6 Z"/></svg>
    </p>

    <address class="address">
      Zorana Medaka 14. Birkenhofweg 9b<br>
      26480 Velin Brod. 3356 Haselbrunn<br>
      Serbia. Austria
    </address>
  </section>

</main>
</body>
</html>
```